'Pellingham Video' - Website Template Design (that I can use in Word Press)

I would like a professional, colorful website template (4 pages) designed in a format that can be used with Word Press. Upon completion of the design, I would like to take over and maintain/host using Web Press and my Go Daddy account.

My business is videography - producing videos for companies, organizations and not-for-profit charities. Our company will do everything, including writing, planning, producing, directing filming and editing videos etc.

I have a colorful logo and business card already designed and I would like the website built around the look of the logo and business card.

I would like an index page designed first. Once the designer has created an index page I like best, I would like three more pages created with that same design.

1) A 'contact us' page
2) A page with a plug in that would allow me to upload video or connect to YouTube to show samples of my videography
3) A general template page I could add new pages to in the future.

Target Market(s)

businesses of all kinds, organizations, governments, not-for-profit charities

Industry/Entity Type

Film Production

Number of Pages Required

4 page

Font styles to use
Sans Serif

Requirements
Must have
• 1) Index page
• 2) Contact Us page
• 2) A page with a plug in that would allow me to upload video or connect to YouTube to show samples of my videography
• 3) A general template page I could add new pages to in the future
Nice to have
• Surprise me! I love lots of color and am open to creative ideas.

```html
<!DOCTYPE html>
<html lang="en">
<head>
<meta charset="utf-8">
<title>Pellingham Video</title>
<link href="https://fonts.googleapis.com/css2?family=Ubuntu:wght@400;500;700&family=Lato:wght@400;700&display=swap" rel="stylesheet">
<style>
:root{
  --black:#000;
  --topbar:#0b0b0b;
  --blue:#0a8fe0;
  --blue-dark:#0a6fc2;
  --blue-light:#26a6f2;
  --yellow:#ffe600;
  --red:#e0232b;
  --orange:#f26a21;
  --indigo:#3950a4;
  --purple:#7b3a96;
  --card-blue:#3a54a6;
  --card-orange:#f26522;
  --card-green:#a3cd3b;
  --footer:#333;
  --footer-bottom:#161616;
  --text:#fff;
  --muted:#d6d6d6;
  --btn:#1a1a1a;
}
*{box-sizing:border-box;margin:0;padding:0}
html,body{width:1200px;height:2264px;overflow:hidden;background:var(--black)}
body{position:relative;font-family:'Lato',sans-serif;color:var(--text)}
.abs{position:absolute}
h1,h2,h3,.nav,.brand{font-family:'Ubuntu',sans-serif}

/* top bar + header */
.topbar{left:0;top:0;width:1200px;height:39px;background:var(--topbar)}
.topbar .social{left:628px;top:12px;display:flex;gap:22px}
.topbar .social span{width:13px;height:13px;border-radius:50%;background:var(--red);display:block}
.topbar .divider{left:762px;top:6px;width:1px;height:27px;background:#333}
.topbar .contact{left:780px;top:10px;font-size:14px;display:flex;gap:18px;align-items:center}
.topbar .contact b{font-weight:700}
.topbar svg{vertical-align:-2px;margin-right:8px}
.header{left:0;top:39px;width:1200px;height:101px;background:linear-gradient(90deg,var(--blue-dark),var(--blue) 45%,var(--blue-light))}
.brand{left:98px;top:14px;display:flex;flex-direction:column;align-items:center;gap:8px}
.brand .mark{width:70px;height:70px;background:var(--blue-dark);border:3px solid #0c2f55}
.brand .name{font-weight:700;font-size:22px;color:#10233f;letter-spacing:.5px}
.nav{left:582px;top:39px;height:101px;display:flex;font-size:14px;font-weight:500}
.nav a{color:#fff;text-decoration:none;display:flex;align-items:center;justify-content:center;height:101px}
.nav .active{background:var(--blue-light);width:67px;margin-right:34px}
.nav .item{width:114px}

/* hero */
.hero{left:0;top:140px;width:1200px;height:471px;background:linear-gradient(180deg,#bfbfbd 0%,#9aa29c 30%,#4f5c53 65%,#26302a 100%)}
.hero h1{position:absolute;left:0;width:1200px;top:250px;text-align:center;font-size:33px;font-weight:700;line-height:41px;text-shadow:0 2px 6px rgba(0,0,0,.5)}
.dots{left:529px;top:425px;display:flex;gap:13px}
.dots span{width:11px;height:11px;background:#fff}
.dots span.on{background:var(--blue)}

/* section titles */
.title{width:1200px;left:0;text-align:center;font-size:30px;font-weight:700}
.title em{font-style:normal;color:var(--yellow)}
.tick{width:30px;height:30px;left:585px;background:var(--red);border:2px solid var(--yellow)}

/* welcome */
.welcome{left:0;top:611px;width:1200px;height:370px;background:var(--black)}
.welcome .deco{left:32px;top:44px;width:208px;height:190px;background:#1b1b1b;opacity:.8}
.welcome p{left:101px;top:131px;width:562px;font-size:12.6px;line-height:24.5px;color:#eee}
.btn{display:flex;align-items:center;justify-content:center;background:var(--btn);border-bottom:3px solid var(--red);font-size:13px;font-weight:700;color:#fff;height:31px}
.welcome .btn{left:99px;top:300px;width:95px}
.video{left:708px;top:136px;width:393px;height:199px;border:1px solid #666;background:linear-gradient(135deg,#d89a5a,#8b6a4e 40%,#3a3f44 70%,#1f2a33)}
.play{left:168px;top:69px;width:56px;height:56px;border-radius:50%;background:rgba(255,255,255,.55)}

/* services */
.services{left:0;top:981px;width:1200px;height:444px;background:linear-gradient(180deg,#6f98c2,#7ea4c5 50%,#8aa6bb)}
.service{top:134px;width:260px;text-align:center}
.service .circle{width:94px;height:94px;border-radius:50%;margin:0 auto;border:3px solid rgba(255,255,255,.4);display:flex;align-items:center;justify-content:center}
.service h3{font-size:22px;font-weight:700;margin-top:16px}
.service p{font-size:12.8px;line-height:24px;margin-top:6px;color:#fff}
.service .btn{width:95px;margin:12px auto 0}
.arrow{top:236px}

/* work for */
.work{left:0;top:1425px;width:1200px;height:567px;background:var(--black)}
.work .deco{left:958px;top:40px;width:210px;height:190px;background:#1b1b1b;opacity:.8}
.card{top:129px;width:308px;height:350px;border-radius:14px;overflow:hidden;text-align:center}
.card .photo{height:177px}
.card h3{font-size:21px;font-weight:700;margin-top:14px}
.card p{font-size:12.8px;line-height:24px;margin:8px 24px 0}
.card svg{margin-top:6px}

/* footer */
.footer{left:0;top:1992px;width:1200px;height:214px;background:var(--footer)}
.inquiry{left:107px;top:1960px;width:266px;height:220px;background:var(--blue-dark)}
.inquiry h2{position:absolute;left:14px;top:8px;font-size:21px;font-weight:400}
.inquiry .rule{position:absolute;left:14px;top:40px;width:238px;height:1px;background:rgba(255,255,255,.4)}
.field{position:absolute;left:14px;width:240px;height:30px;background:#fff;color:#777;font-size:11px;padding:6px 8px}
.submit{position:absolute;left:14px;top:173px;width:86px;height:30px;background:#fff;color:var(--blue-dark);font-size:15px;display:flex;align-items:center;justify-content:center}
.fh{font-family:'Ubuntu',sans-serif;font-size:17px;font-weight:500}
.links{left:410px;top:2014px}
.links ul{list-style:none;margin-top:25px;font-size:12px;line-height:24px}
.cinfo{left:548px;top:2014px}
.cinfo .rule{position:absolute;left:0;top:32px;width:300px;height:1px;background:#555}
.map{left:548px;top:2060px;width:190px;height:130px;background:#2a2a2a;border-radius:30px}
.addr{left:640px;top:2063px;width:180px;height:52px;background:#1a1a1a;font-size:10.5px;padding:5px 8px;line-height:14px}
.addr b{font-size:13px;display:block;margin-bottom:2px}
.cline{left:614px;font-size:12px;display:flex;align-items:center;gap:12px}
.news{left:886px;top:2014px;width:214px}
.news .rule{margin-top:10px;height:1px;background:#555}
.news p{font-size:11.5px;margin-top:11px}
.news .email{margin-top:8px;height:31px;background:#fff;color:#444;font-size:11px;padding:8px 10px}
.news .sub{margin-top:10px;width:88px;height:31px;background:#000;border-bottom:3px solid var(--red);font-size:11.5px;font-weight:700;display:flex;align-items:center;justify-content:center}
.bottom{left:0;top:2206px;width:1200px;height:58px;background:var(--footer-bottom)}
.bottom .social{left:108px;top:14px;display:flex;gap:12px}
.bottom .social span{width:27px;height:27px;border-radius:50%;background:#6a6a6a}
.bottom .social span.on{background:var(--blue)}
.bottom small{position:absolute;right:98px;top:20px;font-size:11.5px}
</style>
</head>
<body>

<div class="abs topbar">
  <div class="abs social"><span></span><span></span><span></span><span></span></div>
  <div class="abs divider"></div>
  <div class="abs contact">
    <span><svg width="12" height="12" viewBox="0 0 24 24"><path fill="#e0232b" d="M6.6 10.8a15 15 0 0 0 6.6 6.6l2.2-2.2c.3-.3.7-.4 1-.2 1.1.4 2.3.6 3.6.6.6 0 1 .4 1 1V20c0 .6-.4 1-1 1A17 17 0 0 1 3 4c0-.6.4-1 1-1h3.5c.6 0 1 .4 1 1 0 1.3.2 2.5.6 3.6.1.3 0 .7-.2 1z"/></svg><b>555-014-2286</b></span>
    <span><svg width="14" height="11" viewBox="0 0 14 11"><rect x=".5" y=".5" width="13" height="10" fill="none" stroke="#e0232b"/><path d="M.5 .5 7 6l6.5-5.5" fill="none" stroke="#e0232b"/></svg>info@pellinghamvideo.com</span>
  </div>
</div>

<div class="abs header"></div>
<div class="abs brand"><div class="mark"></div><div class="name">PELLINGHAM VIDEO</div></div>
<nav class="abs nav">
  <a class="active" href="#">Home</a>
  <a class="item" href="#">About Us</a>
  <a class="item" href="#">Services</a>
  <a class="item" href="#">Gallery</a>
  <a class="item" href="#">Contact</a>
</nav>

<section class="abs hero" role="img" aria-label="Misty pine forest photograph">
  <h1>Our Business Is Producing Videos For Companies,<br>Organizations And Not-for-profit Charities</h1>
  <div class="abs dots"><span class="on"></span><span></span><span></span><span></span><span></span><span></span></div>
</section>

<section class="abs welcome">
  <div class="abs deco" aria-hidden="true"></div>
  <h2 class="abs title" style="top:40px">Welcome to <em>Pellingham video</em></h2>
  <div class="abs tick" style="top:86px"></div>
  <p class="abs">Lorem ipsum dolor sit amet, consectetuer adipiscing elit, sed diam nonummy nibh euismod tincidunt ut laoreet dolore magna aliquam erat volutpat. Ut wisi enim ad minim veniam, quis nostrud exerci tation ullamcorper suscipit lobortis nisl ut aliquip ex ea commodo consequat. Duis autem vel eum iriure dolor in hendrerit in vulputate velit esse molestie consequat, vel illum dolore eu feugiat nulla facilisis at vero eros et accumsan et iusto odio dignissim qui blandit praesent luptatum zzril delenit augue duis dolore te feugait nulla facilisi.</p>
  <div class="abs btn">Read More</div>
  <div class="abs video" role="img" aria-label="Video still of a camera filming a waterfall at sunset">
    <div class="abs play"><svg width="56" height="56" viewBox="0 0 56 56"><path d="M23 19v18l14-9z" fill="#e0232b"/></svg></div>
  </div>
</section>

<section class="abs services" role="img" aria-label="Background photograph of a child playing with a toy plane">
  <h2 class="abs title" style="top:38px">Our Services</h2>
  <div class="abs tick" style="top:82px"></div>
  <svg class="abs arrow" style="left:54px" width="14" height="28" viewBox="0 0 14 28"><path d="M12 2 2 14l10 12" fill="none" stroke="rgba(255,255,255,.6)" stroke-width="2"/></svg>
  <svg class="abs arrow" style="left:1130px" width="14" height="28" viewBox="0 0 14 28"><path d="m2 2 10 12L2 26" fill="none" stroke="rgba(255,255,255,.6)" stroke-width="2"/></svg>

  <div class="abs service" style="left:84px">
    <div class="circle" style="background:var(--orange)"><svg width="40" height="40" viewBox="0 0 40 40"><path d="M8 32l3-9 16-16 6 6-16 16z" fill="none" stroke="#fff" stroke-width="2.5"/></svg></div>
    <h3>Writing</h3>
    <p>Lorem ipsum dolor sit amet,<br>consectetuer adipiscing elit, sed diam<br>nonummy nibh euismod tincidunt ut</p>
    <div class="btn">Read More</div>
  </div>
  <div class="abs service" style="left:342px">
    <div class="circle" style="background:var(--indigo)"><svg width="40" height="40" viewBox="0 0 40 40"><circle cx="20" cy="18" r="8" fill="none" stroke="#fff" stroke-width="2.5"/><path d="M16 29h8M17 33h6M20 4v3M8 8l2 2M32 8l-2 2M4 18h3M33 18h3" stroke="#fff" stroke-width="2.5"/></svg></div>
    <h3>Planning</h3>
    <p>Lorem ipsum dolor sit amet,<br>consectetuer adipiscing elit, sed diam<br>nonummy nibh euismod tincidunt ut</p>
    <div class="btn">Read More</div>
  </div>
  <div class="abs service" style="left:600px">
    <div class="circle" style="background:var(--red)"><svg width="40" height="40" viewBox="0 0 40 40"><circle cx="18" cy="18" r="13" fill="#fff"/><circle cx="18" cy="11" r="3" fill="#e0232b"/><circle cx="18" cy="25" r="3" fill="#e0232b"/><circle cx="11" cy="18" r="3" fill="#e0232b"/><circle cx="25" cy="18" r="3" fill="#e0232b"/><path d="M28 30q6 4 10 0" fill="none" stroke="#fff" stroke-width="2"/></svg></div>
    <h3>Producing</h3>
    <p>Lorem ipsum dolor sit amet,<br>consectetuer adipiscing elit, sed diam<br>nonummy nibh euismod tincidunt ut</p>
    <div class="btn">Read More</div>
  </div>
  <div class="abs service" style="left:857px">
    <div class="circle" style="background:var(--purple)"><svg width="40" height="40" viewBox="0 0 40 40"><path d="M9 8h22v9H9zM11 20h18M12 20l16 14M28 20 12 34" fill="none" stroke="#fff" stroke-width="2.5"/></svg></div>
    <h3>Directing Filming</h3>
    <p>Lorem ipsum dolor sit amet,<br>consectetuer adipiscing elit, sed diam<br>nonummy nibh euismod tincidunt ut</p>
    <div class="btn">Read More</div>
  </div>
</section>

<section class="abs work">
  <div class="abs deco" aria-hidden="true"></div>
  <h2 class="abs title" style="top:36px">We Work for</h2>
  <div class="abs tick" style="top:82px"></div>

  <div class="abs card" style="left:100px;background:var(--card-blue)">
    <div class="photo" role="img" aria-label="Photograph of a cheering group of business people" style="background:linear-gradient(180deg,#f4f4f4,#cfd3d8)"></div>
    <h3>Organizations</h3>
    <p>Lorem ipsum dolor sit amet, consectetuer adipiscing elit, sed diam nonummy nibh euismod tincidunt ut</p>
    <svg width="16" height="10" viewBox="0 0 16 10"><path d="m2 2 6 6 6-6" fill="none" stroke="#fff" stroke-width="2"/></svg>
  </div>
  <div class="abs card" style="left:442px;background:var(--card-orange)">
    <div class="photo" role="img" aria-label="Photograph of two officials reviewing a tablet" style="background:linear-gradient(135deg,#e8e2da,#8c8f96 60%,#3b4150)"></div>
    <h3>Governments</h3>
    <p>Lorem ipsum dolor sit amet, consectetuer adipiscing elit, sed diam nonummy nibh euismod tincidunt ut</p>
    <svg width="16" height="10" viewBox="0 0 16 10"><path d="m2 2 6 6 6-6" fill="none" stroke="#fff" stroke-width="2"/></svg>
  </div>
  <div class="abs card" style="left:792px;background:var(--card-green)">
    <div class="photo" role="img" aria-label="Photograph of a note reading non profit" style="background:linear-gradient(135deg,#7a5a48,#e9e6e0 40%,#d8d3cb)"></div>
    <h3>Not-for-profit Charities</h3>
    <p>Lorem ipsum dolor sit amet, consectetuer adipiscing elit, sed diam nonummy nibh euismod tincidunt ut</p>
    <svg width="16" height="10" viewBox="0 0 16 10"><path d="m2 2 6 6 6-6" fill="none" stroke="#fff" stroke-width="2"/></svg>
  </div>
</section>

<footer class="abs footer"></footer>

<div class="abs inquiry">
  <h2>Quick Inquiry</h2>
  <div class="rule"></div>
  <div class="field" style="top:51px">Name</div>
  <div class="field" style="top:88px">Email</div>
  <div class="field" style="top:125px;height:38px">Case Detail</div>
  <div class="submit">Submit</div>
</div>

<div class="abs links">
  <div class="fh">Quick Links</div>
  <ul><li>Home</li><li>About Us</li><li>Services</li><li>Gallery</li><li>Contact Us</li></ul>
</div>

<div class="abs cinfo"><div class="fh">Contact Info</div><div class="rule"></div></div>
<div class="abs map" role="img" aria-label="Faint world map"></div>
<svg class="abs" style="left:612px;top:2066px" width="14" height="20" viewBox="0 0 14 20"><path d="M7 0a7 7 0 0 0-7 7c0 5 7 13 7 13s7-8 7-13a7 7 0 0 0-7-7z" fill="#fff"/><circle cx="7" cy="7" r="2.5" fill="#333"/></svg>
<div class="abs addr"><b>Pellingham video</b>Lorem ipsum, Dolor amet,<br>Harrowfield - 0148265.</div>
<div class="abs cline" style="top:2128px"><svg width="14" height="14" viewBox="0 0 24 24"><path fill="#fff" d="M6.6 10.8a15 15 0 0 0 6.6 6.6l2.2-2.2c.3-.3.7-.4 1-.2 1.1.4 2.3.6 3.6.6.6 0 1 .4 1 1V20c0 .6-.4 1-1 1A17 17 0 0 1 3 4c0-.6.4-1 1-1h3.5c.6 0 1 .4 1 1 0 1.3.2 2.5.6 3.6.1.3 0 .7-.2 1z"/></svg>555-014-2286</div>
<div class="abs cline" style="top:2156px"><svg width="14" height="11" viewBox="0 0 14 11"><rect width="14" height="11" fill="#fff"/><path d="M0 0l7 6 7-6" fill="none" stroke="#333"/></svg>info@pellinghamvideo.com</div>

<div class="abs news">
  <div class="fh">Newsletter Sign Up</div>
  <div class="rule"></div>
  <p>Stay updated with latest news from</p>
  <div class="email">Enter your Email</div>
  <div class="sub">SUBSCRIBE</div>
</div>

<div class="abs bottom">
  <div class="abs social"><span class="on"></span><span></span><span></span><span></span></div>
  <small>Copyright© 2016 Pellingham Video. All rights reserved.</small>
</div>

</body>
</html>
```